Kestrel Electrical Business Card

We need a business card design for our family-run electrical contracting business based in Western Australia called 'Kestrel Electrical'. We provide electrical services including residential, commercial and industrial. We aim for individual business cards to be made for all of our employees. We already have a company logo, which we require to be featured on the design. We would like simple, sleek and vibrant designs, which incorporate our logo and represent our business. We do not want anything involving too many graphics/images. We like the colours red, black, white and all shades of grey. The final design should communicate professionalism and trustworthiness.
We require the following contact information:
Name- Owen Strickland
EC 5809
Mobile number- 0455 918 302
Fax number (including area code)- (08) 9640 2718
Email adress- name@kestrelelectrical.example
Electrical
- ITC Handel Bold

```html
<!DOCTYPE html>
<html lang="en">
<head>
<meta charset="utf-8">
<title>Kestrel Electrical – Business Card</title>
<link href="https://fonts.googleapis.com/css2?family=Lato:wght@400;700;900&family=Michroma&display=swap" rel="stylesheet">
<style>
  :root {
    --backdrop: #d2d3d5;
    --card: #ffffff;
    --red: #e6202d;
    --ink: #231f20;
    --grey: #7a7a7c;
    --faint: #efefef;
  }
  * { box-sizing: border-box; margin: 0; padding: 0; }
  html, body {
    width: 1200px; height: 1000px; overflow: hidden;
    background: var(--backdrop);
    font-family: "Lato", Arial, sans-serif;
  }
  .card {
    position: absolute; left: 120px; top: 206px;
    width: 960px; height: 588px;
    background: var(--card);
    box-shadow: 0 10px 30px rgba(0,0,0,0.18);
    overflow: hidden;
  }
  .brand {
    position: absolute; left: 80px; top: 84px;
    display: flex; align-items: center; gap: 16px;
    white-space: nowrap;
  }
  .brand-mark { width: 50px; height: 50px; background: var(--ink); flex: none; }
  .brand-name {
    font-weight: 900; font-size: 40px; color: var(--ink);
    letter-spacing: 1px; line-height: 1;
  }
  .watermark-block {
    position: absolute; left: 720px; top: 36px;
    width: 170px; height: 150px;
    background: var(--faint);
  }
  .person {
    position: absolute; right: 70px; top: 232px; text-align: right;
  }
  .person-name { font-weight: 700; font-size: 30px; color: var(--ink); }
  .person-role { font-size: 17px; color: var(--grey); margin-top: 4px; }
  .contacts {
    position: absolute; left: 120px; top: 330px;
    list-style: none;
  }
  .contacts li {
    display: flex; align-items: center; gap: 14px;
    font-size: 25px; color: var(--ink); height: 33px;
    white-space: nowrap;
  }
  .contacts svg { width: 20px; height: 20px; flex: none; }
  .address {
    position: absolute; left: 120px; top: 440px;
    font-size: 25px; color: var(--grey);
    white-space: nowrap;
  }
  .web-band {
    position: absolute; left: 0; bottom: 0;
    width: 100%; height: 100px;
    background: var(--red);
    display: flex; align-items: center; justify-content: center;
  }
  .web-address {
    font-family: "Michroma", "Arial Black", sans-serif;
    color: #fff; font-size: 28px; letter-spacing: 9px;
    white-space: nowrap;
  }
</style>
</head>
<body>
  <div class="card">
    <div class="brand">
      <span class="brand-mark"></span>
      <span class="brand-name">KESTREL ELECTRICAL</span>
    </div>

    <div class="watermark-block" aria-hidden="true"></div>

    <div class="person">
      <div class="person-name">Owen Strickland</div>
      <div class="person-role">Director</div>
    </div>

    <ul class="contacts">
      <li>
        <svg viewBox="0 0 20 20" aria-hidden="true"><rect x="5" y="1" width="10" height="18" rx="2" fill="none" stroke="#e6202d" stroke-width="2"/><circle cx="10" cy="15.5" r="1.2" fill="#e6202d"/></svg>
        0455 918 302
      </li>
      <li>
        <svg viewBox="0 0 20 20" aria-hidden="true"><rect x="2" y="6" width="16" height="12" rx="1.5" fill="#e6202d"/><rect x="5" y="2" width="10" height="6" fill="#e6202d"/><rect x="6" y="10" width="8" height="5" fill="#fff"/></svg>
        (08) 9640 2718
      </li>
      <li>
        <svg viewBox="0 0 20 20" aria-hidden="true"><rect x="1" y="4" width="18" height="12" fill="#e6202d"/><path d="M1 4 L10 11 L19 4" fill="none" stroke="#fff" stroke-width="1.6"/></svg>
        name@kestrelelectrical.example
      </li>
    </ul>

    <div class="address">18 Carrow Street, Bayview WA 6150</div>

    <div class="web-band">
      <span class="web-address">www.kestrelelectrical.example</span>
    </div>
  </div>
</body>
</html>
```